Creative Brief
Brand Packaging Identity V
KALSO
Pose your way
Innovation and Creativity are the cornerstones in the foundation of KALSO. The most accurate quartz watches in the industry, ruggedized for use by those that live, work and play in truly adverse conditions. Water and Shock resistant, the line of technology used is advanced and inventive at the same time, for those whose usage demanded certain durability.
Jewelry
the back dial should consist of some art work as shown as an example in the briefing.

```html
<!DOCTYPE html>
<html lang="en">
<head>
<meta charset="utf-8">
<title>KALSO Packaging Identity</title>
<link rel="stylesheet" href="https://fonts.googleapis.com/css2?family=Cinzel:wght@500&family=Montserrat:wght@400;500&display=swap">
<style>
:root{
  --ink:#111111;
  --ink-soft:#1c1c1c;
  --gold:#b9a57e;
  --gold-dark:#8f7d58;
  --silver-light:#f1f1f1;
  --silver:#c9c9c9;
  --silver-dark:#8a8a8a;
  --paper:#ffffff;
  --line:#d8d8d8;
}
*{box-sizing:border-box;margin:0;padding:0}
html,body{width:1200px;height:1104px;overflow:hidden;background:var(--paper)}
body{position:relative;font-family:"Montserrat",sans-serif;color:var(--gold)}
.piece{position:absolute}
.black{background:var(--ink)}
.brand{font-family:"Cinzel",serif;font-weight:500;color:var(--gold);letter-spacing:.08em;display:flex;align-items:center;gap:.4em;white-space:nowrap}
.brand .dot{width:.55em;height:.55em;border-radius:50%;background:var(--gold)}
.center{display:flex;align-items:center;justify-content:center}
.rot90{transform:rotate(90deg)}
.rot270{transform:rotate(-90deg)}
.rot180{transform:rotate(180deg)}
.url{font-size:9px;letter-spacing:.12em;color:var(--ink)}
.gold-band{position:absolute;left:0;right:0;background:var(--gold);display:flex;align-items:center;justify-content:center}
.fold{border:1px solid #2a2a2a}
.window-strip{background:var(--paper);border:1px solid var(--line);display:flex;gap:6px;align-items:center;padding:0 8px}
.window-strip span{width:30px;height:14px;background:var(--ink)}
.handle-hole{position:absolute;background:var(--paper);border-radius:22px}
.tag{background:var(--ink);clip-path:polygon(50% 0,100% 30%,100% 100%,0 100%,0 30%)}
.tag-hole{position:absolute;width:8px;height:8px;border-radius:50%;background:var(--paper);left:50%;margin-left:-4px}
.banner-silver{background:linear-gradient(90deg,var(--silver-light),var(--silver) 60%,var(--silver-dark))}
.banner-black{background:var(--ink)}
.banner-silver .brand{color:var(--gold-dark)}
.card-text{font-size:9px;color:var(--gold);letter-spacing:.08em}
.field{height:1px;background:var(--gold-dark);margin:10px 0 4px}
.photo{background:linear-gradient(135deg,#f4f4f4,#b8b8b8 55%,#c9a987)}
.dial{position:absolute;width:72px;height:72px;border-radius:50%;background:radial-gradient(circle,#5a5a5a 0 30%,#d9d9d9 34%,#f7f7f7 48%,#9a9a9a 70%,#e8e8e8 100%);box-shadow:0 0 0 2px #bcbcbc}
</style>
</head>
<body>

<!-- Large box dieline -->
<section class="box-dieline">
  <div class="piece black fold center" style="left:99px;top:45px;width:225px;height:45px"><div class="brand rot180" style="font-size:12px"><span class="dot"></span>KALSO</div></div>
  <div class="piece black fold center" style="left:30px;top:105px;width:69px;height:315px"><div class="brand rot90" style="font-size:14px"><span class="dot"></span>KALSO</div></div>
  <div class="piece black fold center" style="left:99px;top:90px;width:225px;height:330px">
    <div class="brand" style="font-size:26px"><span class="dot"></span>KALSO</div>
    <div class="gold-band" style="bottom:0;height:14px"><span class="url">www.kalsowatches.com</span></div>
  </div>
  <div class="piece black fold center" style="left:324px;top:105px;width:66px;height:315px"><div class="brand rot270" style="font-size:14px"><span class="dot"></span>KALSO</div></div>
  <div class="piece window-strip" style="left:99px;top:420px;width:225px;height:30px"><span></span><span></span><span></span><span></span><span></span></div>
</section>

<!-- Paper bag flat -->
<section class="paper-bag">
  <svg class="piece" style="left:540px;top:42px" width="210" height="52" viewBox="0 0 210 52"><path d="M10 52 Q105 -20 200 52" fill="none" stroke="#111" stroke-width="3"/></svg>
  <div class="piece black fold center" style="left:420px;top:90px;width:60px;height:210px"><div class="brand rot270" style="font-size:14px"><span class="dot"></span>KALSO</div></div>
  <div class="piece black fold center" style="left:480px;top:90px;width:330px;height:210px">
    <div class="brand" style="font-size:26px"><span class="dot"></span>KALSO</div>
    <div class="gold-band" style="bottom:0;height:12px"><span class="url">www.kalsowatches.com</span></div>
  </div>
</section>

<!-- Shopping bag -->
<section class="shopping-bag">
  <div class="piece black center" style="left:846px;top:45px;width:324px;height:465px">
    <div class="handle-hole" style="left:102px;top:22px;width:120px;height:44px"></div>
    <div class="brand" style="font-size:34px;margin-top:-40px"><span class="dot"></span>KALSO</div>
    <div class="gold-band" style="bottom:26px;height:14px"><span class="url">www.kalsowatches.com</span></div>
  </div>
</section>

<!-- Small box dieline -->
<section class="small-box">
  <div class="piece black fold center" style="left:408px;top:390px;width:152px;height:90px"><div class="brand rot180" style="font-size:14px"><span class="dot"></span>KALSO</div></div>
  <div class="piece black fold center" style="left:339px;top:480px;width:69px;height:120px"><div class="brand rot90" style="font-size:12px"><span class="dot"></span>KALSO</div></div>
  <div class="piece black fold center" style="left:408px;top:480px;width:152px;height:120px"><div class="brand" style="font-size:18px"><span class="dot"></span>KALSO</div></div>
  <div class="piece black fold center" style="left:560px;top:480px;width:70px;height:120px"><div class="brand rot270" style="font-size:12px"><span class="dot"></span>KALSO</div></div>
  <div class="piece black fold center" style="left:408px;top:600px;width:152px;height:90px"><div class="brand" style="font-size:14px"><span class="dot"></span>KALSO</div></div>
</section>

<!-- Hang tags -->
<section class="hang-tags">
  <div class="piece tag center" style="left:666px;top:410px;width:70px;height:80px"><div class="tag-hole" style="top:14px"></div><div class="brand" style="font-size:10px;margin-top:20px">KALSO</div></div>
  <div class="piece tag center" style="left:750px;top:410px;width:70px;height:80px"><div class="tag-hole" style="top:14px"></div><div class="brand" style="font-size:10px;margin-top:20px">KALSO</div></div>
  <div class="piece tag center" style="left:690px;top:540px;width:40px;height:135px"><div class="tag-hole" style="top:12px"></div><div class="brand rot270" style="font-size:11px">KALSO</div></div>
  <div class="piece tag center" style="left:742px;top:540px;width:40px;height:135px;background:var(--ink-soft)"><div class="tag-hole" style="top:12px"></div><div class="card-text rot270">Swiss Quartz</div></div>

  <div class="piece tag center" style="left:336px;top:730px;width:40px;height:120px"><div class="tag-hole" style="top:12px"></div><div class="brand rot270" style="font-size:10px">KALSO</div></div>
  <div class="piece tag center" style="left:384px;top:730px;width:40px;height:120px"><div class="tag-hole" style="top:12px"></div><div class="card-text rot270">Water Resistant</div></div>
  <div class="piece tag center" style="left:495px;top:720px;width:45px;height:150px"><div class="tag-hole" style="top:12px"></div><div class="brand rot270" style="font-size:11px">KALSO</div></div>
  <div class="piece tag center" style="left:555px;top:720px;width:45px;height:150px"><div class="tag-hole" style="top:12px"></div><div class="brand rot270" style="font-size:11px">KALSO</div></div>
  <div class="piece tag center" style="left:648px;top:770px;width:60px;height:100px"><div class="tag-hole" style="top:12px"></div><div class="brand" style="font-size:10px;margin-top:16px">KALSO</div></div>
  <div class="piece tag center" style="left:720px;top:770px;width:60px;height:100px"><div class="tag-hole" style="top:12px"></div><div class="brand" style="font-size:10px;margin-top:16px">KALSO</div></div>
</section>

<!-- Banners -->
<section class="banners">
  <div class="piece banner-silver center" style="left:846px;top:534px;width:72px;height:366px"><div class="brand rot270" style="font-size:22px"><span class="dot"></span>KALSO</div></div>
  <div class="piece banner-black center" style="left:924px;top:534px;width:72px;height:366px"><div class="brand rot270" style="font-size:22px"><span class="dot"></span>KALSO</div></div>
  <div class="piece banner-silver center" style="left:1020px;top:534px;width:72px;height:366px"><div class="brand rot270" style="font-size:22px"><span class="dot"></span>KALSO</div></div>
  <div class="piece banner-black center" style="left:1104px;top:534px;width:72px;height:366px"><div class="brand rot270" style="font-size:22px"><span class="dot"></span>KALSO</div></div>
</section>

<!-- Warranty cards and watch photos -->
<section class="cards">
  <div class="piece black center" style="left:30px;top:560px;width:135px;height:100px"><div class="brand" style="font-size:14px"><span class="dot"></span>KALSO</div></div>
  <div class="piece black" style="left:180px;top:555px;width:135px;height:145px;padding:14px">
    <div class="card-text">Warranty Card</div>
    <div class="field"></div><div class="card-text">Model</div>
    <div class="field"></div><div class="card-text">Serial</div>
    <div class="field"></div><div class="card-text">Date</div>
  </div>
  <div class="piece photo" role="img" aria-label="Product photographs of KALSO watches" style="left:30px;top:714px;width:285px;height:156px"></div>

  <div class="piece" style="left:30px;top:888px;width:135px;height:90px;border:1px solid var(--line)">
    <div class="gold-band" style="top:0;height:10px"></div>
    <div class="center" style="height:100%"><div class="brand" style="font-size:14px;color:var(--ink)">KALSO</div></div>
  </div>
  <div class="piece black center" style="left:180px;top:888px;width:135px;height:90px"><div class="brand" style="font-size:14px"><span class="dot"></span>KALSO</div></div>
  <div class="piece photo" role="img" aria-label="Row of KALSO watch product photographs" style="left:30px;top:990px;width:285px;height:90px"></div>
</section>

<!-- Watch back dial artwork -->
<section class="dials">
  <div class="dial" role="img" aria-label="Engraved watch back dial artwork" style="left:490px;top:925px"></div>
  <div class="dial" role="img" aria-label="Engraved watch back dial artwork" style="left:570px;top:925px"></div>
  <div class="dial" role="img" aria-label="Engraved watch back dial artwork" style="left:490px;top:1008px"></div>
  <div class="dial" role="img" aria-label="Engraved watch back dial artwork" style="left:570px;top:1008px"></div>

  <div class="dial" role="img" aria-label="Engraved watch back dial artwork" style="left:670px;top:925px"></div>
  <div class="dial" role="img" aria-label="Engraved watch back dial artwork" style="left:750px;top:925px"></div>
  <div class="dial" role="img" aria-label="Engraved watch back dial artwork" style="left:670px;top:1008px"></div>
  <div class="dial" role="img" aria-label="Engraved watch back dial artwork" style="left:750px;top:1008px"></div>

  <div class="dial" role="img" aria-label="Engraved watch back dial artwork" style="left:850px;top:925px"></div>
  <div class="dial" role="img" aria-label="Engraved watch back dial artwork" style="left:930px;top:925px"></div>
  <div class="dial" role="img" aria-label="Engraved watch back dial artwork" style="left:850px;top:1008px"></div>
  <div class="dial" role="img" aria-label="Engraved watch back dial artwork" style="left:930px;top:1008px"></div>

  <div class="dial" role="img" aria-label="Engraved watch back dial artwork" style="left:1020px;top:925px"></div>
  <div class="dial" role="img" aria-label="Engraved watch back dial artwork" style="left:1100px;top:925px"></div>
  <div class="dial" role="img" aria-label="Engraved watch back dial artwork" style="left:1020px;top:1008px"></div>
  <div class="dial" role="img" aria-label="Engraved watch back dial artwork" style="left:1100px;top:1008px"></div>
</section>

</body>
</html>
```